Website improvements and Adding Functionalities at https://vornet.site/pelmarq

1.Search functionality
2.Payment process functionality
3. Application configuration
4. Registration functionality activation
5. Chat functionality
6.Language switching functionality (Portuguese & French)
7.Bespoke interactive modules
8. Automated web scraping and data synchronisation mechanisms
9. News Page
10.Webinar facilities
11. Basic SEO optimisation
12. Speed and performance optimisation
13. Security configuration
14. Google Analytics integration
15. Cross-browser and mobile testing
16. Website deployment and launch support

Target Market(s)

My target markets are companies, investors, suppliers and professionals with an interest in the Mozambican oil and gas sector

Industry/Entity Type

Oil and Gas

Coding

Coded - Design and coding required

Number of Pages Required

1 page

Requirements
Must have
• Improve the existing page at https://vornet.site/pelmarq and add the following features to it: 1. Search functionality 2. Payment process functionality 3. Application configuration 4. Activation of registration functionality 5. Chat functionality 6. Language switching functionality (Portuguese & French) 7. Bespoke interactive modules 8. Automated web scraping and data synchronisation mechanisms 9. News Page

```html
<!DOCTYPE html>
<html lang="en">
<head>
<meta charset="utf-8">
<title>Pelmarq – Search</title>
<link rel="stylesheet" href="https://fonts.googleapis.com/css2?family=Inter:wght@400;500;600;700&display=swap">
<style>
:root{
  --sidebar:#0f1b2a;
  --sidebar-line:#1e2b3b;
  --sidebar-text:#b7c0cc;
  --sidebar-muted:#6f7b8a;
  --active-bg:#0f3b3c;
  --accent:#14c7a8;
  --ink:#111827;
  --muted:#5b6472;
  --page:#f2f5f8;
  --card:#ffffff;
  --line:#dfe3e8;
}
*{box-sizing:border-box;margin:0;padding:0}
html,body{width:1200px;height:533px;overflow:hidden}
body{font-family:"Inter",sans-serif;background:var(--page);color:var(--ink);display:flex}
.sidebar{width:211px;height:533px;background:var(--sidebar);position:relative;flex:none}
.brand{display:flex;align-items:center;gap:8px;height:65px;padding:0 18px;border-bottom:1px solid var(--sidebar-line)}
.brand-mark{width:30px;height:30px;border-radius:7px;background:var(--accent)}
.brand-name{font-size:14px;font-weight:700;color:#fff}
.nav-label{font-size:8.5px;font-weight:600;letter-spacing:.4px;color:var(--sidebar-muted);padding:14px 18px 6px}
.nav{list-style:none;padding:0 11px}
.nav-item{display:flex;align-items:center;gap:10px;height:32px;padding:0 10px;margin-bottom:1.5px;border-radius:6px;font-size:12.5px;font-weight:500;color:var(--sidebar-text)}
.nav-item svg{width:16px;height:16px;stroke:currentColor;fill:none;stroke-width:1.6;stroke-linecap:round;stroke-linejoin:round}
.nav-item.active{background:var(--active-bg);color:var(--accent)}
.badge{margin-left:auto;background:var(--accent);color:#0f1b2a;font-size:8px;font-weight:700;width:17px;height:13px;border-radius:7px;display:flex;align-items:center;justify-content:center;margin-right:1px}
.user{position:absolute;left:0;right:0;bottom:0;height:71px;border-top:1px solid var(--sidebar-line);display:flex;align-items:center;gap:9px;padding:0 19px}
.avatar{width:28px;height:28px;border-radius:50%;background:var(--accent);color:#0f1b2a;font-size:10.5px;font-weight:700;display:flex;align-items:center;justify-content:center}
.user-name{font-size:11px;font-weight:700;color:#fff}
.user-role{font-size:9px;color:var(--sidebar-muted);margin-top:1px}
.main{flex:1;display:flex;flex-direction:column}
.topbar{height:51px;background:#fff;border-bottom:1px solid var(--line);display:flex;align-items:center;padding:0 25px 0 24px}
.topbar-title{font-size:13px;font-weight:700}
.lang{margin-left:auto;display:flex;gap:11px;align-items:center}
.lang-pill{height:27px;padding:0 10px;border-radius:14px;border:1px solid var(--line);background:#fff;font-size:11px;font-weight:600;color:var(--muted);display:flex;align-items:center;gap:3px}
.lang-pill small{font-size:6.5px;font-weight:700}
.lang-pill.active{background:var(--accent);border-color:var(--accent);color:#0f1b2a}
.bell{width:31px;height:31px;border:1px solid var(--line);border-radius:6px;display:flex;align-items:center;justify-content:center;position:relative}
.bell svg{width:15px;height:15px;stroke:var(--ink);fill:none;stroke-width:1.6}
.bell .dot{position:absolute;top:8px;right:9px;width:4px;height:4px;border-radius:50%;background:#ef4444}
.content{padding:30px 25px 0 24px}
.page-title{font-size:17px;font-weight:700}
.page-sub{font-size:11px;color:var(--muted);margin-top:6px}
.search-box{margin-top:18px;height:41px;border:2px solid #3b4350;border-radius:8px;background:#fff;display:flex;align-items:center;gap:11px;padding:0 13px;font-size:12.5px;color:#7a828e}
.search-box svg{width:15px;height:15px;stroke:#4b5563;fill:none;stroke-width:1.8}
.filters{display:flex;gap:7px;margin-top:23px}
.chip{height:24px;padding:0 12px;border-radius:12px;border:1px solid var(--line);background:#fff;font-size:11px;font-weight:500;color:#374151;display:flex;align-items:center}
.chip.active{background:var(--ink);border-color:var(--ink);color:#fff;font-weight:600}
.results{margin-top:18px;background:var(--card);border:1px solid var(--line);border-radius:8px;height:136px;padding:22px 22px 0}
.results-head{display:flex;align-items:center;justify-content:space-between}
.count{font-size:11px;color:var(--muted)}
.sort{width:88px;height:23px;border:1px solid #c9ced6;border-radius:4px;font-size:11px;display:flex;align-items:center;justify-content:space-between;padding:0 6px 0 9px}
.sort svg{width:9px;height:9px;stroke:var(--ink);fill:none;stroke-width:2.4}
.result{display:flex;align-items:center;gap:12px;margin-top:20px}
.result-thumb{width:33px;height:33px;border-radius:6px;background:linear-gradient(135deg,#e7f8ee,#d3efe0)}
.result-title{font-size:11.5px;font-weight:600}
.result-meta{font-size:9.5px;color:var(--muted);margin-top:5px}
</style>
</head>
<body>
<aside class="sidebar">
  <div class="brand"><span class="brand-mark"></span><span class="brand-name">Pelmarq</span></div>
  <div class="nav-label">PLATFORM</div>
  <ul class="nav">
    <li class="nav-item active"><svg viewBox="0 0 24 24"><circle cx="11" cy="11" r="7"/><path d="M20 20l-4-4"/></svg>Search</li>
    <li class="nav-item"><svg viewBox="0 0 24 24"><rect x="3" y="5" width="18" height="14" rx="2"/><path d="M3 10h18"/></svg>Payment</li>
    <li class="nav-item"><svg viewBox="0 0 24 24"><circle cx="12" cy="12" r="3"/><path d="M12 2v3M12 19v3M2 12h3M19 12h3M4.9 4.9l2.1 2.1M17 17l2.1 2.1M4.9 19.1L7 17M17 7l2.1-2.1"/></svg>Configuration</li>
    <li class="nav-item"><svg viewBox="0 0 24 24"><circle cx="9" cy="8" r="4"/><path d="M2 21c0-4 3-6 7-6s7 2 7 6M16 11l2 2 4-4"/></svg>Registration</li>
    <li class="nav-item"><svg viewBox="0 0 24 24"><path d="M4 4h16v12H8l-4 4z"/></svg>Chat<span class="badge">3</span></li>
    <li class="nav-item"><svg viewBox="0 0 24 24"><circle cx="12" cy="12" r="9"/><path d="M3 12h18M12 3c3 3 3 15 0 18M12 3c-3 3-3 15 0 18"/></svg>Language</li>
    <li class="nav-item"><svg viewBox="0 0 24 24"><rect x="3" y="3" width="7" height="7"/><rect x="14" y="3" width="7" height="7"/><rect x="3" y="14" width="7" height="7"/><rect x="14" y="14" width="7" height="7"/></svg>Modules</li>
    <li class="nav-item"><svg viewBox="0 0 24 24"><path d="M4 20L20 4M14 4h6v6M4 14v6h6"/></svg>Data Sync</li>
  </ul>
  <div class="user">
    <div class="avatar">ID</div>
    <div><div class="user-name">Ines Dorval</div><div class="user-role">Administrator</div></div>
  </div>
</aside>
<div class="main">
  <header class="topbar">
    <div class="topbar-title">Search</div>
    <div class="lang">
      <span class="lang-pill active"><small>GB</small> EN</span>
      <span class="lang-pill"><small>PT</small> PT</span>
      <span class="lang-pill"><small>FR</small> FR</span>
      <span class="bell"><svg viewBox="0 0 24 24"><path d="M6 16V11a6 6 0 0112 0v5l2 2H4zM10 21h4"/></svg><span class="dot"></span></span>
    </div>
  </header>
  <main class="content">
    <h1 class="page-title">Search</h1>
    <p class="page-sub">Find records, documents, users and transactions across the platform.</p>
    <div class="search-box"><svg viewBox="0 0 24 24"><circle cx="11" cy="11" r="7"/><path d="M20 20l-4-4"/></svg>Search users, orders, documents...</div>
    <div class="filters">
      <span class="chip">All</span><span class="chip">Users</span><span class="chip">Orders</span><span class="chip">Documents</span><span class="chip active">Products</span>
    </div>
    <section class="results">
      <div class="results-head">
        <span class="count">Showing 1 result</span>
        <span class="sort">Relevance<svg viewBox="0 0 12 12"><path d="M2 4l4 4 4-4"/></svg></span>
      </div>
      <div class="result">
        <div class="result-thumb" role="img" aria-label="Product icon: clipboard"></div>
        <div>
          <div class="result-title">Pelmarq Enterprise Suite</div>
          <div class="result-meta">Product · SaaS · Active · 3 variants</div>
        </div>
      </div>
    </section>
  </main>
</div>
</body>
</html>
```